Webdesign for Dutch IT consultancy company

Make a Wordpress webdesign for a Dutch consultancy company

Briefing Brivola IT

Website for finding and connecting IT-professionals. Corebusiness is to find IT-professionals and to help them to follow their ambitions. We offer training, personal coaching and education trajects.

U can take www.Tavemko.nl as an example for the website.

Home page

U can take www.Tavemko.nl as an example.

There should be jobs on the home page. A block for short info about us and about what whe do and a trigger to contact us quickly.

Jobs Page

On this page should be the jobs that we offer for the professionals. There should be a search function on this page so u can easily find the job that you are looking for.

A call to action can be on this page too.

Also a little block with text for some information.

For professionals page

Block with information on top. Call to action. info about who we work for/with.

For Clients

Info about three different solutions

- Sourcing solutions
- Consultancy solutions
- Custom based traineeships

Request a qoute option

Traineeships page

Info about two different traineeships

- Linux traineeships
- Microsoft traineeships

Call to action/ subscribe for traineeships

About us page

We are BrivolaT IT

Our mission: Creating cooperations between young professionals and businesses who wanna work on a great future.

Our core values

Last news

Target Market(s)

Young professionals and businesses who need IT services

Industry/Entity Type

It Company

Coding

Coded - Design and coding required

Number of Pages Required

5+ page

Font styles to use
Other font styles liked:
• Calibri

Colors
ffffff
add136
6b449b

Requirements
Must have
• Home page, Jobs Page, Professionals page, Clients page, Traineeships page, About us Page
• Green and/or Purple layout. Job search option, subscribe option
Nice to have
• modern design

```html
<!DOCTYPE html>
<html lang="en">
<head>
<meta charset="utf-8">
<title>Brivola IT – Sourcing and Consultancy</title>
<link rel="stylesheet" href="https://fonts.googleapis.com/css2?family=Ubuntu:wght@400;500;700&family=Roboto:wght@400;500;700&display=swap">
<style>
:root{
  --purple:#7b2d8e;
  --purple-dark:#63207a;
  --green:#a5cd39;
  --dark:#333333;
  --darker:#242424;
  --text:#555555;
  --muted:#888888;
  --light:#f1f1f1;
  --white:#ffffff;
}
*{box-sizing:border-box;margin:0;padding:0}
html,body{width:1200px;height:4580px;overflow:hidden}
body{position:relative;font-family:"Roboto",Arial,sans-serif;color:var(--text);background:var(--white)}
.abs{position:absolute}
h1,h2,h3,h4{font-family:"Ubuntu",Arial,sans-serif}
.accent{color:var(--green)}
.purple{color:var(--purple)}

/* top bar */
.topbar{left:0;top:0;width:1200px;height:43px;background:var(--dark)}
.topbar-mail{left:742px;top:12px;color:#ddd;font-size:14px;display:flex;align-items:center;gap:8px}
.topbar-phone{left:998px;top:0;width:122px;height:52px;background:var(--purple);color:#fff;font-size:17px;display:flex;align-items:center;justify-content:center;gap:8px;font-weight:500}

/* nav */
.logo{font-family:"Ubuntu",sans-serif;font-weight:700;font-size:36px;color:var(--purple);display:flex;align-items:center;gap:10px;letter-spacing:1px}
.logo-dot{width:24px;height:24px;border-radius:50%;background:var(--green)}
.header-logo{left:76px;top:78px}
.nav{left:390px;top:92px;width:730px;display:flex;justify-content:space-between;font-size:15px;color:#666;text-transform:uppercase}

/* hero */
.hero{left:0;top:152px;width:1200px;height:590px;background:linear-gradient(135deg,#4a4f57 0%,#6d737b 40%,#3d4148 100%)}
.hero-shade{left:0;top:152px;width:1200px;height:590px;background:rgba(20,22,28,.45)}
.hero-title{left:0;top:384px;width:1200px;text-align:center;color:#fff;font-size:40px;font-weight:700;letter-spacing:1px}
.hero-sub{left:0;top:442px;width:1200px;text-align:center;color:#eee;font-size:17px}
.btn{display:flex;align-items:center;justify-content:center;border-radius:22px;font-size:15px;font-weight:500;text-transform:uppercase;color:#fff;height:40px}
.btn-outline{left:418px;top:492px;width:177px;border:2px solid #fff}
.btn-green{left:604px;top:492px;width:177px;background:var(--green)}

/* welcome */
.welcome-title{left:0;top:786px;width:1200px;text-align:center;font-size:44px;font-weight:700;color:var(--purple)}
.welcome-text{left:174px;top:852px;width:852px;text-align:center;font-size:15px;line-height:22px;color:var(--text)}

/* search */
.search{left:0;top:1008px;width:1200px;height:238px;background:var(--green)}
.search-title{left:0;top:1056px;width:1200px;text-align:center;color:#fff;font-size:38px;font-weight:700}
.field{background:#fff;height:52px;display:flex;align-items:center;justify-content:space-between;padding:0 16px;font-size:14px;color:#777;border-radius:2px}
.field-job{left:174px;top:1128px;width:415px}
.field-loc{left:607px;top:1128px;width:236px}
.search-submit{left:864px;top:1128px;width:162px;height:52px;background:var(--purple);color:#fff;font-size:16px;font-weight:700;display:flex;align-items:center;justify-content:center;text-transform:uppercase}

/* categories */
.cat{top:1300px;width:210px;height:192px;background:#fff;border:2px solid #e3e3e3;box-shadow:0 2px 6px rgba(0,0,0,.08);display:flex;flex-direction:column;align-items:center;padding-top:36px}
.cat-name{margin-top:18px;font-size:19px;color:#333}
.cat-count{margin-top:6px;font-size:14px;color:var(--muted)}

/* job board */
.board-title{left:0;top:1518px;width:1200px;text-align:center;font-size:44px;font-weight:700;color:var(--purple)}
.board{left:76px;top:1581px;width:1044px;border-collapse:collapse;font-size:14px}
.board th{background:var(--purple);color:#fff;font-weight:400;font-size:17px;height:52px;text-align:left}
.board td{height:52px;color:#444}
.board th:first-child,.board td:first-child{padding-left:16px;width:525px}
.board th:nth-child(2){width:177px}
.board th:nth-child(3){width:187px}
.board tr:nth-child(even) td{background:var(--light)}
.full{color:var(--purple)}
.part{color:#333}

/* about band */
.about-band{left:0;top:2045px;width:1200px;height:449px;background:linear-gradient(90deg,#c6d8e6 0%,#e3ecf3 45%,#d7e1ea 100%)}
.info-card{top:2171px;width:352px;height:210px;background:#fff;box-shadow:0 2px 8px rgba(0,0,0,.12)}
.info-card h3{position:absolute;left:66px;top:40px;font-size:20px;font-weight:500;color:#333;text-transform:uppercase}
.info-card p{position:absolute;left:66px;top:76px;width:232px;font-size:14px;line-height:20px;color:#555}
.info-icon{position:absolute;left:20px;top:36px}
.read-strip{position:absolute;right:0;top:0;width:44px;height:210px;background:var(--dark);display:flex;align-items:center;justify-content:center}
.read-strip span{transform:rotate(-90deg);white-space:nowrap;color:#fff;font-family:"Ubuntu",sans-serif;font-weight:700;font-size:17px;letter-spacing:1px}

/* stats */
.stat{top:2560px;width:356px;text-align:center}
.stat-num{font-family:"Ubuntu",sans-serif;font-weight:700;font-size:56px;color:#555;letter-spacing:2px}
.stat-label{margin-top:6px;font-size:17px;color:#555}
.stat-bar{width:55px;height:4px;background:var(--purple);margin:26px auto 0}
.stat-divider{top:2572px;width:1px;height:118px;background:#ddd}

/* jobs section */
.jobs-photo{left:76px;top:2772px;width:562px;height:458px;background:linear-gradient(135deg,#cfd4d9 0%,#a9b1ba 50%,#e3e6e9 100%)}
.jobs-label{left:76px;top:3160px;width:220px;height:70px;background:var(--green);color:#333;font-family:"Ubuntu",sans-serif;font-weight:700;font-size:34px;display:flex;align-items:center;padding-left:24px}
.job-icon{left:626px;width:80px;height:80px;border-radius:50%;background:var(--purple);border:4px solid #fff;display:flex;align-items:center;justify-content:center}
.job-item{left:723px;width:400px}
.job-item h4{font-size:21px;font-weight:700;color:#333}
.job-item p{margin-top:8px;font-size:14px;line-height:20px;color:#555}
.job-links{margin-top:8px;font-size:13px;font-weight:700;color:var(--purple);display:flex;gap:16px}
.job-links span{border-bottom:2px solid var(--purple)}

/* quote */
.quote{left:0;top:3328px;width:1200px;height:467px;background:#efefef}
.quote-title{left:76px;top:3400px;font-size:44px;font-weight:700;color:var(--purple)}
.quote-text{left:76px;top:3470px;width:530px;font-size:14px;line-height:20px;color:#555}
.q-input{width:220px;height:46px;background:#fff;border:1px solid #ddd;font-size:14px;color:#666;display:flex;align-items:center;padding-left:14px}
.q-submit{left:76px;top:3676px;width:159px;height:49px;background:var(--purple);color:#fff;font-size:16px;font-weight:700;display:flex;align-items:center;justify-content:center}
.quote-photo{left:626px;top:3358px;width:488px;height:437px;background:linear-gradient(180deg,#f3f3f3 0%,#d7e2ef 60%,#c2d3e8 100%)}

/* blog */
.blog-title{left:0;top:3832px;width:1200px;text-align:center;font-size:44px;font-weight:700;color:var(--purple)}
.blog-card{top:3908px;width:324px;height:226px;background:#f3f3f3;border:1px solid #e3e3e3;padding:50px 18px 0}
.blog-card h4{font-size:21px;font-weight:500;color:#333}
.blog-card p{margin-top:12px;font-size:15px;line-height:21px;color:#555}
.blog-meta{margin-top:16px;padding-top:14px;border-top:1px solid #ddd;display:flex;justify-content:space-between;font-size:13px;color:#666}
.blog-meta span{display:flex;align-items:center;gap:6px}

/* footer */
.footer{left:0;top:4222px;width:1200px;height:290px;background:var(--dark)}
.footer-logo-box{left:76px;top:4222px;width:324px;height:113px;background:var(--darker);display:flex;align-items:center;justify-content:center}
.footer-logo-box .logo{color:#fff}
.footer-head{font-family:"Ubuntu",sans-serif;font-weight:700;font-size:19px;color:var(--green);text-transform:uppercase}
.newsletter-head{left:76px;top:4374px;color:#fff;font-family:"Ubuntu",sans-serif;font-weight:500;font-size:17px;text-transform:uppercase}
.newsletter{left:76px;top:4421px;width:324px;height:42px;background:#fff;display:flex;align-items:center;justify-content:space-between;padding:0 14px;font-size:14px;color:#999;font-style:italic}
.f-list{list-style:none;color:#ddd;font-size:15px}
.f-list li{display:flex;align-items:flex-start;gap:12px;line-height:20px}
.services{left:440px;top:4334px}
.services li{margin-bottom:17px}
.contact{left:800px;top:4334px}
.bottombar{left:0;top:4512px;width:1200px;height:68px;background:var(--darker);display:flex;align-items:center;justify-content:space-between;padding:0 76px;color:#ccc;font-size:14px}
.bottombar b{color:#fff}
.to-top{width:42px;height:42px;border-radius:50%;border:2px solid #888;display:flex;align-items:center;justify-content:center}
</style>
</head>
<body>

<!-- top bar -->
<div class="abs topbar"></div>
<div class="abs topbar-mail">
  <svg width="16" height="12" viewBox="0 0 16 12"><rect x="0.5" y="0.5" width="15" height="11" fill="#fff"/><path d="M1 1l7 6 7-6" fill="none" stroke="#333" stroke-width="1.2"/></svg>
  info@brivolait.com
</div>
<div class="abs topbar-phone">
  <svg width="16" height="16" viewBox="0 0 24 24"><path d="M6.6 10.8a15 15 0 006.6 6.6l2.2-2.2a1 1 0 011-.25 11.4 11.4 0 003.6.6 1 1 0 011 1V20a1 1 0 01-1 1A17 17 0 013 4a1 1 0 011-1h3.5a1 1 0 011 1c0 1.25.2 2.45.57 3.57a1 1 0 01-.25 1z" fill="#fff"/></svg>
  123 456 7890
</div>

<!-- header -->
<div class="abs header-logo logo"><span class="logo-dot"></span>BRIVOLA IT</div>
<nav class="abs nav">
  <span>Home</span><span>About Us</span><span>Jobs</span><span>Professionals</span><span>Clients</span><span>Traineeships</span><span>Contact</span>
</nav>

<!-- hero -->
<div class="abs hero" role="img" aria-label="Photo of a team meeting in a bright office"></div>
<div class="abs hero-shade"></div>
<h1 class="abs hero-title">BRIVOLA IT SOURCING AND CONSULTANCY</h1>
<p class="abs hero-sub">connecting IT-professionals and personal coaching.</p>
<div class="abs btn btn-outline">Know More</div>
<div class="abs btn btn-green">Contact Us</div>

<!-- welcome -->
<h2 class="abs welcome-title">WELCOME TO <span class="accent">BRIVOLAT IT</span></h2>
<p class="abs welcome-text">Lorem ipsum dolor sit amet, consectetur adipiscing elit. Etiam fringilla odio in mollis tincidunt. Morbi tempus purus mi, a mattis turpis maximus non. Suspendisse semper posuere sapien sit amet dignissim. Etiam et quam ut ex varius eleifend eget nec purus. Suspendisse eget lorem nulla. Aenean et ullamcorper mauris. Mauris aliquam non ipsum eu accumsan. Nam cursus neque eu turpis dapibus tincidunt.</p>

<!-- search -->
<div class="abs search"></div>
<h2 class="abs search-title">SEARCH JOB</h2>
<div class="abs field field-job">Job Title*<svg width="14" height="8" viewBox="0 0 14 8"><path d="M1 1l6 6 6-6" fill="none" stroke="#777" stroke-width="1.6"/></svg></div>
<div class="abs field field-loc">Location*<svg width="14" height="8" viewBox="0 0 14 8"><path d="M1 1l6 6 6-6" fill="none" stroke="#777" stroke-width="1.6"/></svg></div>
<div class="abs search-submit">Submit</div>

<!-- categories -->
<div class="abs cat" style="left:104px">
  <svg width="60" height="50" viewBox="0 0 60 50" fill="none" stroke="#7b2d8e" stroke-width="2"><rect x="4" y="4" width="44" height="32" rx="2"/><path d="M18 44h16M26 36v8"/><rect x="38" y="22" width="18" height="24" rx="2"/><path d="M12 14h18M12 22h12"/></svg>
  <div class="cat-name">Web Designer</div><div class="cat-count">(13 Job)</div>
</div>
<div class="abs cat" style="left:363px">
  <svg width="60" height="50" viewBox="0 0 60 50" fill="none" stroke="#7b2d8e" stroke-width="2.4"><path d="M18 13L6 25l12 12M42 13l12 12-12 12"/><circle cx="24" cy="25" r="1.6" fill="#7b2d8e"/><circle cx="30" cy="25" r="1.6" fill="#7b2d8e"/><circle cx="36" cy="25" r="1.6" fill="#7b2d8e"/></svg>
  <div class="cat-name">Web Developer</div><div class="cat-count">(13 Job)</div>
</div>
<div class="abs cat" style="left:623px">
  <svg width="60" height="50" viewBox="0 0 60 50" fill="none" stroke="#7b2d8e" stroke-width="2"><rect x="16" y="4" width="24" height="42" rx="3"/><path d="M25 40h6"/><circle cx="44" cy="16" r="8"/><path d="M44 12v8M40 16h8"/></svg>
  <div class="cat-name">App Developer</div><div class="cat-count">(13 Job)</div>
</div>
<div class="abs cat" style="left:882px">
  <svg width="60" height="50" viewBox="0 0 60 50" fill="none" stroke="#7b2d8e" stroke-width="2"><rect x="6" y="14" width="48" height="32" rx="3"/><path d="M22 14V8h16v6M6 28h48M27 28v5h6v-5"/></svg>
  <div class="cat-name">Sales Manager</div><div class="cat-count">(13 Job)</div>
</div>

<!-- job board -->
<h2 class="abs board-title">JOB <span class="accent">BOARD</span></h2>
<table class="abs board">
  <thead><tr><th>Job Title</th><th>Location</th><th>Category</th><th>Full/Part Time</th></tr></thead>
  <tbody>
    <tr><td>Lorem ipsum dolor sit amet, consectetur adipiscing elit.</td><td>New zealand</td><td>Web Design</td><td class="full">Full Time</td></tr>
    <tr><td>Lorem ipsum dolor sit amet, adipiscing elit.</td><td>New zealand</td><td>Web Development</td><td class="part">Part Time</td></tr>
    <tr><td>Lorem ipsum dolor sit amet, consectetur adipiscing elit.</td><td>New zealand</td><td>Web Design</td><td class="part">Part Time</td></tr>
    <tr><td>Lorem ipsum dolor sit amet, adipiscing elit.</td><td>New zealand</td><td>Web Development</td><td class="part">Part Time</td></tr>
    <tr><td>Lorem ipsum dolor sit amet, consectetur adipiscing elit.</td><td>New zealand</td><td>Web Design</td><td class="full">Full Time</td></tr>
    <tr><td>Lorem ipsum dolor sit amet, consectetur adipiscing elit.</td><td>New zealand</td><td>Web Development</td><td class="part">Part Time</td></tr>
  </tbody>
</table>

<!-- about band -->
<div class="abs about-band" role="img" aria-label="Photo of a smiling businesswoman holding a tablet in a bright office"></div>
<div class="abs info-card" style="left:76px">
  <svg class="info-icon" width="32" height="32" viewBox="0 0 32 32" fill="none" stroke="#555" stroke-width="1.8"><circle cx="12" cy="10" r="6"/><path d="M2 30c0-6 4.5-10 10-10s10 4 10 10M24 8h6M24 14h6"/></svg>
  <h3>About Us</h3>
  <p>Lorem ipsum dolor sit amet, consectetur adipiscing elit. Etiam fringilla odio in mollis tincidunt per mauris.</p>
  <div class="read-strip"><span>READ MORE</span></div>
</div>
<div class="abs info-card" style="left:461px">
  <svg class="info-icon" width="32" height="32" viewBox="0 0 32 32" fill="none" stroke="#555" stroke-width="1.8"><rect x="4" y="4" width="20" height="26" rx="2"/><path d="M10 4V2h8v2M9 13l3 3 5-6M9 22h10"/><path d="M28 10v18"/></svg>
  <h3>What We Do</h3>
  <p>Lorem ipsum dolor sit amet, consectetur adipiscing elit. Etiam fringilla odio in mollis tincidunt per mauris.</p>
  <div class="read-strip"><span>READ MORE</span></div>
</div>

<!-- stats -->
<div class="abs stat" style="left:66px"><div class="stat-num">3356</div><div class="stat-label">Happy Customers</div><div class="stat-bar"></div></div>
<div class="abs stat-divider" style="left:422px"></div>
<div class="abs stat" style="left:422px"><div class="stat-num">3356</div><div class="stat-label">Job Posts</div><div class="stat-bar"></div></div>
<div class="abs stat-divider" style="left:778px"></div>
<div class="abs stat" style="left:778px"><div class="stat-num">3356</div><div class="stat-label">Consultations Done</div><div class="stat-bar"></div></div>

<!-- jobs -->
<div class="abs jobs-photo" role="img" aria-label="Photo of a job interview between a businessman and a woman in an office"></div>
<div class="abs jobs-label">JOBS</div>

<div class="abs job-icon" style="top:2820px"><svg width="34" height="30" viewBox="0 0 34 30" fill="none" stroke="#fff" stroke-width="2"><rect x="2" y="2" width="30" height="20" rx="2"/><path d="M12 28h10M17 22v6"/></svg></div>
<div class="abs job-item" style="top:2812px"><h4>IT Vacatures</h4><p>Lorem ipsum dolor sit amet, consectetur adipiscing elit. Etiam fringilla odio in mollis tincidunt per mauris.</p><div class="job-links"><span>READ MORE</span><span>CONTACT US</span></div></div>

<div class="abs job-icon" style="top:2969px"><svg width="34" height="30" viewBox="0 0 34 30" fill="none" stroke="#fff" stroke-width="2"><rect x="2" y="2" width="30" height="20" rx="2"/><path d="M12 28h10M17 22v6"/></svg></div>
<div class="abs job-item" style="top:2961px"><h4>IT Vacatures</h4><p>Lorem ipsum dolor sit amet, consectetur adipiscing elit. Etiam fringilla odio in mollis tincidunt per mauris.</p><div class="job-links"><span>READ MORE</span><span>CONTACT US</span></div></div>

<div class="abs job-icon" style="top:3118px"><svg width="34" height="30" viewBox="0 0 34 30" fill="none" stroke="#fff" stroke-width="2"><rect x="2" y="2" width="30" height="20" rx="2"/><path d="M12 28h10M17 22v6"/></svg></div>
<div class="abs job-item" style="top:3110px"><h4>IT Vacatures</h4><p>Lorem ipsum dolor sit amet, consectetur adipiscing elit. Etiam fringilla odio in mollis tincidunt per mauris.</p><div class="job-links"><span>READ MORE</span><span>CONTACT US</span></div></div>

<!-- quote -->
<div class="abs quote"></div>
<div class="abs quote-photo" role="img" aria-label="Photo of a smiling businesswoman gesturing towards the form"></div>
<h2 class="abs quote-title">REQUEST A <span class="accent">QUICK</span> QUOTE</h2>
<p class="abs quote-text">Please feel free to contact us at the information provided below and we will be sure to get back to you as soon as possible</p>
<div class="abs q-input" style="left:76px;top:3551px">Name</div>
<div class="abs q-input" style="left:314px;top:3551px">Phone No.</div>
<div class="abs q-input" style="left:76px;top:3615px">Email</div>
<div class="abs q-input" style="left:314px;top:3615px">Subject</div>
<div class="abs q-submit">SUBMIT</div>

<!-- blog -->
<h2 class="abs blog-title">LATEST <span class="accent">BLOG</span></h2>
<article class="abs blog-card" style="left:76px"><h4>Blog Title</h4><p>Lorem Ipsum is simply dummy text of the printing and typesetting industry.</p><div class="blog-meta"><span>by admin</span><span><svg width="12" height="12" viewBox="0 0 12 12"><rect x="1" y="2" width="10" height="9" fill="none" stroke="#666"/><path d="M1 5h10" stroke="#666"/></svg>12th April 2017</span></div></article>
<article class="abs blog-card" style="left:433px"><h4>Blog Title</h4><p>Lorem Ipsum is simply dummy text of the printing and typesetting industry.</p><div class="blog-meta"><span>by admin</span><span><svg width="12" height="12" viewBox="0 0 12 12"><rect x="1" y="2" width="10" height="9" fill="none" stroke="#666"/><path d="M1 5h10" stroke="#666"/></svg>12th April 2017</span></div></article>
<article class="abs blog-card" style="left:796px"><h4>Blog Title</h4><p>Lorem Ipsum is simply dummy text of the printing and typesetting industry.</p><div class="blog-meta"><span>by admin</span><span><svg width="12" height="12" viewBox="0 0 12 12"><rect x="1" y="2" width="10" height="9" fill="none" stroke="#666"/><path d="M1 5h10" stroke="#666"/></svg>13th April 2017</span></div></article>

<!-- footer -->
<footer>
<div class="abs footer"></div>
<div class="abs footer-logo-box"><div class="logo"><span class="logo-dot"></span>BRIVOLA IT</div></div>
<div class="abs newsletter-head">Newsletter Signup</div>
<div class="abs newsletter">Email Address<svg width="22" height="18" viewBox="0 0 22 18"><path d="M1 8l20-7-6 16-4-6z" fill="#a5cd39"/></svg></div>

<div class="abs footer-head" style="left:440px;top:4282px">Our Services</div>
<ul class="abs f-list services">
  <li><svg width="16" height="16" viewBox="0 0 16 16"><circle cx="8" cy="8" r="7" fill="none" stroke="#a5cd39" stroke-width="1.5"/><path d="M5 8l2 2 4-4" fill="none" stroke="#a5cd39" stroke-width="1.5"/></svg>Sourcing solutions</li>
  <li><svg width="16" height="16" viewBox="0 0 16 16"><circle cx="8" cy="8" r="7" fill="none" stroke="#a5cd39" stroke-width="1.5"/><path d="M5 8l2 2 4-4" fill="none" stroke="#a5cd39" stroke-width="1.5"/></svg>Consultancy solutions</li>
  <li><svg width="16" height="16" viewBox="0 0 16 16"><circle cx="8" cy="8" r="7" fill="none" stroke="#a5cd39" stroke-width="1.5"/><path d="M5 8l2 2 4-4" fill="none" stroke="#a5cd39" stroke-width="1.5"/></svg>Custom based traineeships</li>
</ul>

<div class="abs footer-head" style="left:800px;top:4282px">Contact Info</div>
<ul class="abs f-list contact">
  <li style="margin-bottom:22px"><svg width="16" height="20" viewBox="0 0 16 20"><path d="M8 0a7 7 0 00-7 7c0 5 7 13 7 13s7-8 7-13a7 7 0 00-7-7z" fill="#a5cd39"/><circle cx="8" cy="7" r="2.5" fill="#333"/></svg>Lorem ipsum dolor sit amet,<br>consectetur adipiscing elit.</li>
  <li style="margin-bottom:22px"><svg width="16" height="16" viewBox="0 0 24 24"><path d="M6.6 10.8a15 15 0 006.6 6.6l2.2-2.2a1 1 0 011-.25 11.4 11.4 0 003.6.6 1 1 0 011 1V20a1 1 0 01-1 1A17 17 0 013 4a1 1 0 011-1h3.5a1 1 0 011 1c0 1.25.2 2.45.57 3.57a1 1 0 01-.25 1z" fill="#a5cd39"/></svg>123 456 7890</li>
  <li><svg width="16" height="12" viewBox="0 0 16 12"><rect x="0" y="0" width="16" height="12" fill="#a5cd39"/><path d="M1 1l7 6 7-6" fill="none" stroke="#333" stroke-width="1.2"/></svg>info@brivolait.com</li>
</ul>

<div class="abs bottombar">
  <span><b>©BRIVOLA IT</b> -2017. All Rights Reserved.</span>
  <span class="to-top"><svg width="16" height="10" viewBox="0 0 16 10"><path d="M1 9l7-7 7 7" fill="none" stroke="#a5cd39" stroke-width="2"/></svg></span>
</div>
</footer>

</body>
</html>
```